Plakate für Glasfaserausbau
Zielgruppe
Informationsbanner für den Start des Glasfaserausbaus in der Straße oder im Ort
Aufgabenstellung
Vorgabe für Plakate im Format von Wahlplakaten und für Banner an Bauzäunen
Enthalten sein, sollen folgende Texte:
Achtung Bauarbeiten!
Hier entsteht das Glasfasernetz der Zukunft
Infohotline: 04172 318-0
glasfasernetz@qv7-lumatel.de
www.qv7-lumatel.de

```html
<!DOCTYPE html>
<html lang="de">
<head>
<meta charset="utf-8">
<title>Achtung Bauarbeiten – Glasfaserausbau</title>
<link rel="stylesheet" href="https://fonts.googleapis.com/css2?family=Roboto+Condensed:wght@700&family=Inter:wght@400;700&display=swap">
<style>
  :root {
    --deep-blue: #1f3560;
    --mid-blue: #2f6f9f;
    --light-blue: #cfe6f3;
    --fibre-glow: #e8f6ff;
    --fibre-blue: #3f88c4;
    --cable-blue: #24457c;
    --white: #ffffff;
    --footer-blue: #1f62ab;
  }
  html, body {
    margin: 0;
    padding: 0;
    overflow: hidden;
    background: var(--white);
  }
  .poster {
    position: relative;
    width: 847px;
    height: 1200px;
    overflow: hidden;
    background: var(--white);
    font-family: "Inter", "Helvetica Neue", Arial, sans-serif;
  }
  .backdrop {
    position: absolute;
    left: 0;
    top: 0;
    width: 847px;
    height: 1110px;
    background:
      radial-gradient(ellipse 50% 40% at 48% 58%, var(--light-blue) 0%, #86bddb 45%, rgba(47,111,159,0) 100%),
      linear-gradient(180deg, var(--deep-blue) 0%, #2b5c8c 28%, #3d84b4 60%, #24487a 100%);
  }
  .fibre-photo {
    position: absolute;
    left: 178px;
    top: 256px;
    width: 496px;
    height: 854px;
    border-radius: 248px 248px 0 0;
    background:
      radial-gradient(ellipse 42% 20% at 50% 24%, var(--fibre-glow) 0%, rgba(232,246,255,0.7) 40%, rgba(232,246,255,0) 100%),
      linear-gradient(180deg, rgba(120,185,230,0.9) 0%, var(--fibre-blue) 45%, var(--cable-blue) 100%);
    -webkit-mask-image: radial-gradient(ellipse 70% 80% at 50% 40%, #000 55%, transparent 100%);
            mask-image: radial-gradient(ellipse 70% 80% at 50% 40%, #000 55%, transparent 100%);
  }
  .headline {
    position: absolute;
    left: 0;
    width: 847px;
    top: 94px;
    margin: 0;
    text-align: center;
    font-family: "Roboto Condensed", "Arial Narrow", sans-serif;
    font-weight: 700;
    font-size: 77px;
    line-height: 1;
    letter-spacing: -0.5px;
    color: var(--white);
  }
  .tagline {
    position: absolute;
    left: 527px;
    top: 755px;
    margin: 0;
    font-weight: 400;
    font-size: 32px;
    line-height: 42px;
    letter-spacing: -0.2px;
    color: var(--white);
  }
  .brand {
    position: absolute;
    left: 47px;
    top: 1012px;
    display: flex;
    align-items: center;
    gap: 10px;
    font-weight: 700;
    font-size: 24px;
    line-height: 1;
    color: var(--white);
  }
  .brand-square {
    width: 20px;
    height: 20px;
    background: var(--white);
  }
  .footer {
    position: absolute;
    left: 0;
    top: 1110px;
    width: 847px;
    height: 90px;
    background: var(--white);
    color: var(--footer-blue);
    font-size: 18.5px;
  }
  .footer span {
    position: absolute;
    top: 35px;
    white-space: nowrap;
  }
  .hotline { left: 47px; }
  .email { left: 286px; }
  .website { left: 584px; font-weight: 700; font-size: 19px; }
  .hotline strong { font-weight: 700; }
</style>
</head>
<body>
  <div class="poster">
    <div class="backdrop"></div>
    <div class="fibre-photo" role="img" aria-label="Foto: leuchtendes, aufgefächertes Bündel aus Glasfaserkabeln, unten zusammengebunden, vor blauem Hintergrund"></div>

    <h1 class="headline">Achtung Bauarbeiten!</h1>

    <p class="tagline">Hier entsteht<br>das Glasfasernetz<br>der Zukunft</p>

    <div class="brand">
      <span class="brand-square"></span>
      <span class="brand-name">QV7 Lumatel</span>
    </div>

    <footer class="footer">
      <span class="hotline">Infohotline <strong>04172 318-0</strong></span>
      <span class="email">glasfasernetz@qv7-lumatel.de</span>
      <span class="website">www.qv7-lumatel.de</span>
    </footer>
  </div>
</body>
</html>
```